Webdesign für KOR GmbH
Zielgruppe
KOR GmbH - Spezialist für Anlasser und Lichtmaschinen
Gegründet 1992 ist KOR nunmehr ein deutschlandweit agierendes Unternehmen mit 13 Mitarbeitern. Der Fokus unserer Arbeit liegt dabei auf der professionellen Regenerierung von Anlassern und Lichtmaschinen. Die strikte Arbeit nach Herstellerstandards und der hohe Anspruch an Qualität und Qualitätssicherung wurde durch die Einführung der ISO Zertifizierung 9001 untermauert.
Der Vertrieb von:
Anlassern
Lichtmaschinen
Turboladern
Klimakompressoren
Verdampfern / Kondensatoren
Batterien
namenhafter Hersteller ergänzt das Portfolio. Die Spezialisierung auf diese Produktgruppen ermöglicht dabei ein hohes Maß an Verfügbarkeit und marktgerechte Preise.
- Modern
- Klares und übersichtliches Desgin
- Nicht zu verspielt
- Informativ
- Leichte Navigation
- Das Design der alten Webseite soll NICHT kopiert werden
- Die Farben des Logos sollen sich wiederfinden

```html
<!DOCTYPE html>
<html lang="de">
<head>
<meta charset="utf-8">
<title>KOR GmbH – Webdesign</title>
<link href="https://fonts.googleapis.com/css2?family=Montserrat:wght@400;500;600;700;800&display=swap" rel="stylesheet">
<style>
:root{
  --green:#0b7a3e;
  --green-bright:#12a04f;
  --green-soft:#e9f5ee;
  --mint:#e6f8ee;
  --ink:#1f2226;
  --muted:#7a7f86;
  --line:#e6e8eb;
  --page:#f4f4f4;
  --light:#f3f4f6;
  --dark:#2a2b2e;
  --footer:#2c2d30;
  --white:#ffffff;
}
*{box-sizing:border-box;margin:0;padding:0}
html,body{width:1200px;height:2645px;overflow:hidden}
body{background:var(--page);font-family:'Montserrat',sans-serif;color:var(--ink);position:relative}
.brand-mark{position:absolute;top:160px;left:0;width:1200px;text-align:center;font-size:64px;font-weight:700;color:var(--green);letter-spacing:1px}
.site{position:absolute;left:229px;top:400px;width:711px;background:var(--white);box-shadow:0 20px 50px rgba(0,0,0,.12)}
.wrap{padding:0 46px;position:relative}
.topbar{height:16px;background:var(--green);color:#dff3e7;font-size:6.5px;display:flex;align-items:center;justify-content:space-between;padding:0 46px}
.topbar span{margin-right:12px;display:inline-flex;align-items:center;gap:4px}
.iso-pill{background:#fff;color:var(--green);border-radius:8px;padding:1px 6px;font-weight:600;font-size:6px}
.nav{height:53px;display:flex;align-items:center;padding:0 46px;justify-content:space-between;border-bottom:1px solid var(--line)}
.logo-text{font-size:11px;font-weight:700;color:var(--green)}
.nav-links{display:flex;gap:17px;font-size:7px;color:#444;margin-left:60px}
.nav-links .active{color:var(--green);font-weight:600}
.btn{display:inline-flex;align-items:center;gap:6px;font-size:7px;font-weight:600;border-radius:2px;padding:0 14px}
.btn-green{background:var(--green);color:#fff}
.btn-white{background:#fff;color:var(--ink);border:1px solid var(--line)}
.hero{height:441px;position:relative;color:#fff;padding:72px 46px 0}
.hero-photo{position:absolute;inset:0;background:linear-gradient(90deg,#242a27 0%,#2f3934 40%,#4a5650 70%,#3a433f 100%)}
.hero-photo::after{content:"";position:absolute;inset:0;background:linear-gradient(90deg,rgba(20,24,22,.75) 0%,rgba(20,24,22,.2) 60%,rgba(20,24,22,.1) 100%)}
.hero>*:not(.hero-photo){position:relative}
.eyebrow{font-size:6.5px;color:#d5dcd8;display:flex;align-items:center;gap:4px}
.eyebrow i{width:5px;height:5px;border-radius:50%;background:var(--green-bright);display:inline-block}
.hero h1{font-size:27px;line-height:28px;font-weight:700;margin-top:16px;width:330px}
.hero h1 em{font-style:normal;color:var(--green)}
.hero p{font-size:9px;line-height:13px;color:#d6dbd8;width:270px;margin-top:14px}
.hero-btns{display:flex;gap:8px;margin-top:16px}
.hero-btns .btn{height:20px}
.hero-btns .blank{width:107px;background:#fff;border-radius:2px}
.checks{display:flex;gap:12px;margin-top:40px;font-size:6.5px;color:#cbd2ce}
.checks span{display:flex;align-items:center;gap:4px}
.stats{height:75px;background:var(--green);display:flex;justify-content:space-around;align-items:center;color:#fff;text-align:center;padding:0 40px}
.stats b{display:block;font-size:16px;font-weight:700}
.stats small{font-size:6.5px;color:#cfe9d9}
.why{background:var(--light);height:267px;padding-top:45px;text-align:center}
.why h2{font-size:16px;font-weight:700}
.why .sub{font-size:8px;line-height:13px;color:var(--muted);width:300px;margin:8px auto 0}
.cards4{display:flex;gap:12px;margin-top:25px;text-align:left}
.card4{flex:1;height:103px;background:#fff;border:1px solid var(--line);border-radius:3px;padding:12px 11px}
.ico{width:20px;height:20px;border-radius:3px;background:var(--green-soft);display:flex;align-items:center;justify-content:center}
.card4 h3{font-size:8px;font-weight:600;margin-top:9px;line-height:12px}
.card4 p{font-size:6.5px;line-height:10px;color:var(--muted);margin-top:6px}
.products{height:370px;padding-top:46px}
.sec-head{display:flex;justify-content:space-between;align-items:flex-start}
.sec-head h2{font-size:16px;font-weight:700}
.sec-head p{font-size:8px;color:var(--muted);margin-top:5px}
.sec-head .btn{height:17px;margin-top:8px;font-weight:500;font-size:6.5px}
.cards3{display:flex;gap:15px;margin-top:23px}
.card3{flex:1;height:223px;border:1px solid var(--line);border-radius:2px;overflow:hidden}
.card3 .img{height:147px}
.img-starter{background:linear-gradient(135deg,#eef0f2,#b8bcc1 60%,#dfe2e5)}
.img-alt{background:linear-gradient(135deg,#3c4a42,#6c7570 50%,#2e3631)}
.img-store{background:linear-gradient(90deg,#2f3a33,#7d8a80 45%,#c9cdca 50%,#7d8a80 55%,#2f3a33)}
.card3 .body{padding:12px 11px}
.card3 h3{font-size:9px;font-weight:600}
.card3 p{font-size:6.5px;line-height:10px;color:var(--muted);margin-top:6px}
.more{font-size:6.5px;font-weight:600;color:var(--green);margin-top:8px;display:flex;gap:4px;align-items:center}
.about{height:388px;background:var(--dark);color:#fff;position:relative}
.about .text{position:absolute;left:46px;top:102px;width:295px}
.kicker{font-size:6px;color:var(--green);font-weight:600;letter-spacing:.5px}
.about h2{font-size:16px;font-weight:700;margin-top:6px}
.about p{font-size:7px;line-height:11.5px;color:#c7c9cc;margin-top:9px}
.feats{display:flex;gap:40px;margin-top:16px}
.feat{display:flex;gap:6px;align-items:flex-start}
.feat .ico{background:#34403a}
.feat b{font-size:7px;font-weight:600;display:block}
.feat small{font-size:6px;color:#9a9ea3}
.about .btn{height:20px;margin-top:18px}
.about-img{position:absolute;left:366px;top:45px;width:298px;height:298px}
.years{position:absolute;left:355px;top:305px;width:74px;height:48px;background:var(--green);padding:10px 11px;border-radius:2px}
.years b{font-size:15px;font-weight:700;display:block}
.years small{font-size:6.5px;color:#d4eedf}
.cta{height:185px;background:var(--mint);text-align:center;padding-top:52px}
.cta h2{font-size:16px;font-weight:700}
.cta p{font-size:8px;line-height:13px;color:var(--muted);width:360px;margin:9px auto 0}
.cta-btns{display:flex;gap:8px;justify-content:center;margin-top:15px}
.cta-btns .btn{height:20px}
.footer{height:180px;background:var(--footer);color:#b8bbbf;padding-top:30px}
.fcols{display:flex}
.fcol{width:164px}
.fcol:first-child{width:164px}
.fcol h4{font-size:8px;color:#fff;font-weight:600;margin-bottom:9px}
.fcol li{list-style:none;font-size:7px;line-height:15px;padding-left:8px}
.fcol .about-txt{font-size:6.5px;line-height:10.5px;margin-top:10px}
.fcol .logo-text{color:#fff;font-size:10px}
.badge{display:inline-block;width:67px;height:10px;background:var(--green);border-radius:1px;margin-top:6px}
.contact li{display:flex;gap:5px;padding-left:0;line-height:11px;margin-bottom:6px}
.fbottom{display:flex;justify-content:space-between;font-size:6px;color:#8b8f94;margin-top:36px}
.fbottom span{margin-left:12px}
</style>
</head>
<body>
<div class="brand-mark">KOR GmbH</div>

<div class="site">
  <div class="topbar">
    <div>
      <span><svg width="7" height="7" viewBox="0 0 24 24" fill="none" stroke="#fff" stroke-width="2"><path d="M5 3h4l2 5-3 2a11 11 0 0 0 6 6l2-3 5 2v4a2 2 0 0 1-2 2A17 17 0 0 1 3 5a2 2 0 0 1 2-2z"/></svg>+49 (0) 123 456 78</span>
      <span><svg width="7" height="7" viewBox="0 0 24 24" fill="none" stroke="#fff" stroke-width="2"><rect x="3" y="5" width="18" height="14" rx="2"/><path d="M3 7l9 6 9-6"/></svg>info@kor-gmbh.de</span>
    </div>
    <span class="iso-pill">ISO 9001 zertifiziert</span>
  </div>

  <div class="nav">
    <div class="logo-text">KOR GmbH</div>
    <div class="nav-links">
      <span class="active">Startseite</span><span>Unternehmen ⌄</span><span>Produkte ⌄</span><span>Instandsetzung ⌄</span><span>Shop</span><span>Kontakt</span>
    </div>
    <span class="btn btn-green" style="height:19px">Anfrage stellen</span>
  </div>

  <section class="hero">
    <div class="hero-photo" role="img" aria-label="Techniker in grauer Arbeitskleidung prüft Lichtmaschinen in einer Werkstatthalle"></div>
    <div class="eyebrow"><i></i>Seit 1992 Ihr zuverlässiger Partner</div>
    <h1>Professionelle Regenerierung und Vertrieb von <em>Anlassern</em> und <em>Lichtmaschinen</em></h1>
    <p>Deutschlandweit tätig. ISO 9001 zertifiziert. Höchste Qualitätsanforderungen und marktgerechte Preise für Werkstätten und Handel.</p>
    <div class="hero-btns">
      <span class="btn btn-green" style="width:121px">Produkte entdecken →</span>
      <span class="blank"></span>
    </div>
    <div class="checks">
      <span>✓ Regenerierung nach Herstellerstandards</span>
      <span>✓ Hohe Verfügbarkeit</span>
      <span>✓ Marktgerechte Preise</span>
    </div>
  </section>

  <div class="stats">
    <div><b>30+</b><small>Jahre Erfahrung</small></div>
    <div><b>10.000+</b><small>Artikel auf Lager</small></div>
    <div><b>100%</b><small>Qualitätsgeprüft</small></div>
    <div><b>24h</b><small>Schnellversand</small></div>
  </div>

  <section class="why">
    <div class="wrap">
      <h2>Warum KOR GmbH?</h2>
      <p class="sub">Über 30 Jahre Erfahrung in der Regenerierung und im Vertrieb von Anlassern und Lichtmaschinen</p>
      <div class="cards4">
        <div class="card4"><div class="ico"><svg width="9" height="9" viewBox="0 0 24 24" fill="none" stroke="#0b7a3e" stroke-width="2"><path d="M12 3l8 3v6c0 5-4 8-8 9-4-1-8-4-8-9V6z"/></svg></div><h3>Herstellerstandards</h3><p>Regenerierung nach höchsten Qualitätsanforderungen und Herstellervorgaben</p></div>
        <div class="card4"><div class="ico"><svg width="9" height="9" viewBox="0 0 24 24" fill="none" stroke="#0b7a3e" stroke-width="2"><circle cx="12" cy="9" r="5"/><path d="M9 13l-1 8 4-2 4 2-1-8"/></svg></div><h3>ISO 9001 zertifiziert</h3><p>Zertifiziertes Qualitätsmanagement für gleichbleibend hohe Produktqualität</p></div>
        <div class="card4"><div class="ico"><svg width="9" height="9" viewBox="0 0 24 24" fill="none" stroke="#0b7a3e" stroke-width="2"><rect x="2" y="7" width="12" height="9"/><path d="M14 10h4l3 3v3h-7"/><circle cx="6" cy="18" r="2"/><circle cx="17" cy="18" r="2"/></svg></div><h3>Hohe Verfügbarkeit</h3><p>Schnelle Lieferung durch umfangreiches Lager mit über 10.000 Artikeln</p></div>
        <div class="card4"><div class="ico"><svg width="9" height="9" viewBox="0 0 24 24" fill="none" stroke="#0b7a3e" stroke-width="2"><path d="M14 6a4 4 0 0 0 5 5L10 20a2 2 0 0 1-3-3l9-9"/></svg></div><h3>Professionelle Instandsetzung</h3><p>Fachgerechte Regenerierung durch erfahrene Spezialisten</p></div>
      </div>
    </div>
  </section>

  <section class="products">
    <div class="wrap">
      <div class="sec-head">
        <div><h2>Unsere Produktkategorien</h2><p>Qualitätsprodukte für Werkstätten und Handel</p></div>
        <span class="btn btn-white">Alle Produkte →</span>
      </div>
      <div class="cards3">
        <div class="card3"><div class="img img-starter" role="img" aria-label="Silberner Anlasser vor hellem Hintergrund"></div><div class="body"><h3>Anlasser</h3><p>Hochwertige Anlasser für PKW, LKW und Nutzfahrzeuge</p><div class="more">Mehr erfahren →</div></div></div>
        <div class="card3"><div class="img img-alt" role="img" aria-label="Lichtmaschine auf einem Prüfstand mit grünen Digitalanzeigen"></div><div class="body"><h3>Lichtmaschinen</h3><p>Zuverlässige Lichtmaschinen für alle Fahrzeugtypen</p><div class="more">Mehr erfahren →</div></div></div>
        <div class="card3"><div class="img img-store" role="img" aria-label="Lagerhalle mit grünen Regalen voller Aggregate"></div><div class="body"><h3>Klimakompressoren</h3><p>Klimatechnik und Zubehör für optimale Fahrzeugklimatisierung</p><div class="more">Mehr erfahren →</div></div></div>
      </div>
    </div>
  </section>

  <section class="about">
    <div class="text">
      <div class="kicker">ÜBER UNS</div>
      <h2>Kompetenz seit 1992</h2>
      <p>Die KOR GmbH ist ein deutschlandweit tätiger Spezialist für die professionelle Regenerierung und den Vertrieb von Anlassern und Lichtmaschinen für PKW, LKW und Nutzfahrzeuge.</p>
      <p>Mit unserem ISO 9001 zertifizierten Qualitätsmanagement garantieren wir höchste Standards bei der Aufarbeitung und Prüfung aller Produkte. Unser umfangreiches Lager sorgt für schnelle Verfügbarkeit und kurze Lieferzeiten.</p>
      <div class="feats">
        <div class="feat"><div class="ico"></div><div><b>Qualität</b><small>ISO 9001 zertifiziert</small></div></div>
        <div class="feat"><div class="ico"></div><div><b>Nachhaltigkeit</b><small>Ressourcenschonend</small></div></div>
      </div>
      <span class="btn btn-green">Mehr über uns →</span>
    </div>
    <div class="about-img img-store" role="img" aria-label="Langer Lagergang mit grünen Regalen voller Anlasser und Lichtmaschinen"></div>
    <div class="years"><b>30+</b><small>Jahre Erfahrung</small></div>
  </section>

  <section class="cta">
    <h2>Benötigen Sie eine Beratung?</h2>
    <p>Unser Expertenteam steht Ihnen für alle Fragen rund um Anlasser, Lichtmaschinen und Instandsetzung zur Verfügung.</p>
    <div class="cta-btns">
      <span class="btn btn-green">Kontakt aufnehmen →</span>
      <span class="btn btn-white">Zum Shop</span>
    </div>
  </section>

  <footer class="footer">
    <div class="wrap">
      <div class="fcols">
        <div class="fcol">
          <div class="logo-text">KOR GmbH</div>
          <p class="about-txt">Ihr zuverlässiger Partner für die professionelle Regenerierung und den Vertrieb von Anlassern und Lichtmaschinen seit 1992.</p>
          <span class="badge"></span>
        </div>
        <div class="fcol"><h4>Produkte</h4><ul><li>Anlasser</li><li>Lichtmaschinen</li><li>Klimakompressoren</li><li>Batterien</li><li>Turbolader</li></ul></div>
        <div class="fcol"><h4>Service</h4><ul><li>Instandsetzung Anlasser</li><li>Instandsetzung Lichtmaschinen</li><li>Online Shop</li><li>Prüfstände</li><li>Kontakt</li></ul></div>
        <div class="fcol contact"><h4>Kontakt</h4><ul>
          <li><span style="color:#12a04f">✆</span>+49 (0) 123 456 78</li>
          <li><span style="color:#12a04f">✉</span>info@kor-gmbh.de</li>
          <li><span style="color:#12a04f">●</span><span>Musterstraße 123<br>12345 Musterstadt<br>Deutschland</span></li>
        </ul></div>
      </div>
      <div class="fbottom">
        <div>© 2026 KOR GmbH. Alle Rechte vorbehalten.</div>
        <div><span>Impressum</span><span>Datenschutz</span><span>AGB</span><span>Downloads</span><span>BFSG</span></div>
      </div>
    </div>
  </footer>
</div>
</body>
</html>
```